www.norvatepastimes.com

Updating website so looks futristic but yet business like and easy to navigate, essentially a good landing page with a cool picture summing up what we do, and links to the following pages, all other pages on site to be updated, Exclusive Distributor of Brimla Flex Unique Fitness Equipment Products in UK & Ireland, www.ferncrestdash.co.uk Exclusive Partners & Distributors Of Ferncrest Dash - Obstacle Races - Obstacle Hire - Obstacle Training - Adventure Events, www.jogvelmora.co.uk Adventures That Inspire. We also Health Club / Facillity Consultancy

```html
<!DOCTYPE html>
<html lang="en">
<head>
<meta charset="utf-8">
<title>Norvate Pastimes – Health, Wellness, Fitness, Consultants</title>
<link href="https://fonts.googleapis.com/css2?family=Marcellus&family=Marcellus+SC&family=Raleway:wght@400;500;600;700;800&display=swap" rel="stylesheet">
<style>
:root{
  --yellow:#e9c60b;
  --yellow-deep:#d7b400;
  --ink:#1b1b1b;
  --night:#111111;
  --text:#5a5a5a;
  --white:#ffffff;
  --field:#ececec;
}
*{box-sizing:border-box;margin:0;padding:0}
html,body{width:1200px;height:4186px;overflow:hidden;background:var(--white)}
body{position:relative;font-family:'Raleway',sans-serif;color:var(--text)}
section,header,footer{position:absolute;left:0;width:1200px}
.abs{position:absolute}
.heading{position:absolute;left:0;width:1200px;text-align:center;font-family:'Marcellus SC',serif;font-size:44px;color:var(--ink);letter-spacing:1px;white-space:nowrap}

/* hero */
.hero{top:0;height:678px;background:linear-gradient(180deg,#3b3d3f 0%,#5c5a55 40%,#3a3633 75%,#241f1c 100%)}
.hero-shade{position:absolute;inset:0;background:rgba(0,0,0,.35)}
.brand{position:absolute;left:98px;top:22px;color:var(--white);white-space:nowrap}
.brand-name{font-family:'Marcellus SC',serif;font-size:44px;line-height:1}
.brand-tag{font-family:'Marcellus',serif;font-size:21px;margin-top:6px}
.nav{position:absolute;top:50px;left:478px;display:flex;flex-wrap:nowrap;white-space:nowrap;font-size:13px;color:var(--white);font-weight:500}
.nav a{color:inherit;text-decoration:none;height:40px;line-height:40px;padding:0 11px}
.nav a.current{border:2px solid var(--yellow);border-radius:22px;color:var(--yellow);line-height:36px;padding:0 14px;margin-right:4px}
.partner-pill{position:absolute;left:958px;top:9px;width:166px;height:40px;border:2px solid var(--yellow);border-radius:22px;color:var(--yellow);font-family:'Marcellus SC',serif;font-size:19px;text-align:center;line-height:36px;white-space:nowrap}
.hero-title{position:absolute;top:268px;width:1200px;text-align:center;color:var(--white);font-size:92px;font-weight:700;white-space:nowrap}
.hero-sub{position:absolute;top:384px;width:1200px;text-align:center;color:var(--white);font-family:'Marcellus',serif;font-size:31px}
.hero-actions{position:absolute;top:441px;left:413px;display:flex}
.btn{display:block;height:56px;line-height:56px;font-family:'Marcellus SC',serif;font-size:22px;border-radius:30px;text-decoration:none;white-space:nowrap}
.btn-solid{background:var(--yellow);color:var(--white);width:190px;text-align:center}
.btn-line{border:2px solid var(--yellow);color:var(--yellow);width:184px;text-align:center;line-height:52px}

/* lead form band */
.lead{top:678px;height:220px;background:var(--yellow)}
.lead .heading{top:42px;font-size:40px}
.lead-field{position:absolute;top:790px;height:53px;background:var(--white);font-size:13px;color:#888;padding:0 16px;line-height:53px}
.lead-submit{position:absolute;top:790px;left:954px;width:168px;height:53px;border:2px solid var(--white);border-radius:30px;color:var(--white);font-family:'Marcellus SC',serif;font-size:22px;text-align:center;line-height:49px}

/* welcome */
.welcome{top:898px;height:840px}
.welcome .heading{top:60px;font-size:42px}
.intro{position:absolute;top:120px;left:168px;width:864px;text-align:center;font-size:14px;line-height:24px}
.video-frame{position:absolute;top:190px;left:75px;width:1047px;height:469px;background:var(--yellow);padding:12px}
.video-still{width:100%;height:100%;background:linear-gradient(135deg,#cfcfcf 0%,#9a9a9a 40%,#4b4b4b 70%,#2b2b2b 100%)}
.play{position:absolute;left:492px;top:202px}
.story{position:absolute;top:686px;left:98px;width:1004px;text-align:center;font-size:13.5px;line-height:24px}

/* expertise */
.expertise{top:1738px;height:490px}
.expertise .heading{top:16px;font-size:42px}
.panel{position:absolute;top:89px;width:400px;height:372px}
.panel-photo{width:100%;height:312px}
.panel-label{height:60px;background:var(--yellow);color:var(--ink);font-family:'Marcellus SC',serif;font-size:30px;text-align:center;line-height:60px}
.panel-feature{background:linear-gradient(180deg,#e4c314,#d4b210);text-align:center;color:var(--white)}
.panel-feature h3{font-family:'Marcellus SC',serif;font-weight:400;font-size:29px;color:var(--ink);padding-top:78px}
.panel-feature p{width:300px;margin:16px auto 0;font-size:15px;line-height:24px}
.panel-more{width:168px;height:47px;margin:44px auto 0;border:2px solid var(--white);border-radius:26px;font-family:'Marcellus SC',serif;font-size:20px;line-height:43px}

/* testimonial */
.testimonial{top:2228px;height:487px}
.testimonial .heading{top:30px;font-size:42px}
.quote-badge{position:absolute;left:567px;top:98px;width:66px;height:66px;border-radius:50%;background:var(--yellow)}
.quote-text{position:absolute;top:186px;left:98px;width:1004px;text-align:center;font-size:13.5px;line-height:26px}
.client{position:absolute;top:353px;left:405px;display:flex;align-items:center;white-space:nowrap}
.client-dot{width:83px;height:83px;border-radius:50%;background:var(--ink)}
.client-info{margin-left:16px}
.client-name{font-family:'Marcellus SC',serif;font-size:22px;color:var(--yellow)}
.client-role{font-size:14px;margin-top:6px;color:var(--text)}
.arrow{position:absolute;top:375px}

/* services */
.services{top:2715px;height:440px}
.services-bar{height:111px;background:linear-gradient(180deg,#161616,#262626)}
.services .heading{top:26px;color:var(--white);font-size:44px}
.tile{position:absolute;top:111px;width:300px;height:265px}
.tile-focus{border:6px solid var(--yellow)}
.zoom{position:absolute;left:122px;top:104px}
.services-rail{position:absolute;top:376px;height:64px;width:1200px;background:var(--yellow)}

/* club */
.club{top:3155px;height:425px}
.club-photo{position:absolute;left:84px;top:67px;width:502px;height:358px;background:radial-gradient(ellipse at 50% 45%,#c9c9c9 0%,#e9e9e9 55%,#ffffff 80%)}
.club-title{position:absolute;left:605px;top:82px;font-family:'Marcellus SC',serif;font-weight:400;font-size:44px;color:var(--ink);white-space:nowrap}
.club-sub{position:absolute;left:605px;top:143px;font-size:14px}
.club-field{position:absolute;left:605px;width:503px;height:51px;border-radius:26px;background:var(--field);font-size:13px;color:#888;padding-left:32px;line-height:51px}
.club-btn{position:absolute;left:605px;top:316px;width:232px;height:50px;border-radius:26px;background:var(--yellow);color:var(--white);font-family:'Marcellus SC',serif;font-size:22px;text-align:center;line-height:50px}

/* consult */
.consult{top:3580px;height:265px;background:linear-gradient(180deg,#dcbc16 0%,#e9c60b 50%,#d2b000 100%)}
.consult .heading{top:52px;font-size:44px}
.consult-sub{position:absolute;top:118px;width:1200px;text-align:center;font-size:16px;color:var(--ink)}
.down{position:absolute;left:569px;top:153px;width:62px;height:62px;border-radius:50%;background:var(--white)}

/* footer */
.footer{top:3845px;height:341px;background:var(--night);color:#cfcfcf;font-size:13px}
.col-title{position:absolute;top:33px;font-family:'Marcellus SC',serif;font-weight:400;font-size:19px;color:var(--yellow)}
.sitemap{position:absolute;left:78px;top:68px;list-style:none;line-height:35.5px;font-size:13px}
.sitemap li::before{content:"» ";color:var(--yellow)}
.sitemap li.current{color:var(--yellow)}
.news{position:absolute;left:340px;width:240px}
.news-thumb{position:absolute;left:0;top:0;width:48px;height:48px;border-radius:50%;background:linear-gradient(135deg,#bfbfbf,#6f6f6f)}
.news p{margin-left:64px;line-height:18px;font-size:12.5px}
.news time{display:block;margin-left:64px;color:var(--yellow);font-size:12px;margin-top:3px}
.contact-row{position:absolute;left:608px;display:flex;align-items:flex-start;gap:16px;font-size:12.5px;line-height:18px}
.foot-brand{position:absolute;left:850px;top:108px;width:320px;text-align:center;white-space:nowrap}
.foot-brand .brand-name{font-size:31px;color:var(--white)}
.foot-brand .brand-tag{font-size:15px;color:var(--white);margin-top:4px}
.foot-brand small{display:block;margin-top:12px;font-size:12.5px;line-height:20px}
.foot-brand small b{color:var(--yellow);font-weight:600}
.social{width:22px;height:22px;border-radius:50%;background:var(--yellow)}
</style>
</head>
<body>

<header class="hero">
  <div class="abs" style="inset:0" role="img" aria-label="Photo of a group fitness class training with kettlebells in a gym"></div>
  <div class="hero-shade"></div>
  <div class="brand">
    <div class="brand-name">Norvate Pastimes</div>
    <div class="brand-tag">Health, Wellness, Fitness, Consultants</div>
  </div>
  <nav class="nav">
    <a class="current" href="#">HOME</a>
    <a href="#">HEALTH</a>
    <a href="#">WELLNESS</a>
    <a href="#">FITNESS</a>
    <a href="#">OUR TEAM</a>
    <a href="#">TESTIMONIALS</a>
    <a href="#">CONTACT</a>
  </nav>
  <div class="partner-pill">Brimla Flex</div>
  <h1 class="hero-title">Ready To Start ?</h1>
  <p class="hero-sub">Health, Wellness, Fitness, Consultants</p>
  <div class="hero-actions">
    <a class="btn btn-solid" href="#">Join Us Now</a>
    <a class="btn btn-line" href="#">More Info</a>
  </div>
</header>

<section class="lead">
  <h2 class="heading">Build Your Business Today</h2>
</section>
<div class="lead-field" style="left:75px;width:212px">Name *</div>
<div class="lead-field" style="left:299px;width:206px">Email *</div>
<div class="lead-field" style="left:516px;width:207px">Subject *</div>
<div class="lead-field" style="left:734px;width:209px">Message *</div>
<div class="lead-submit">Submit</div>

<section class="welcome">
  <h2 class="heading">Welcome To Norvate Pastimes</h2>
  <p class="intro">Norvate Pastimes are leading consultants to the Health, Wellness and Fitness industry, with over 25 years experience working with some of the biggest global worldwide brands from equipment providers and facility operators.</p>
  <div class="video-frame">
    <div class="video-still" role="img" aria-label="Video still of an indoor cycling class riding stationary bikes"></div>
    <svg class="play" width="64" height="64" viewBox="0 0 64 64" aria-hidden="true"><circle cx="32" cy="32" r="32" fill="rgba(0,0,0,.55)"/><path d="M25 19 L46 32 L25 45 Z" fill="#fff"/></svg>
  </div>
  <p class="story">To mass participation events and obstacle course races. Norvate Pastimes is a multi disciplined business specialising in helping brands grow through insight, strategy creation and valuable sector collaboration, recent clients include the exclusive distribution of Brimla Flex bodyweight training products for the UK and Ireland, exclusive distribution of fitness app Kinetra Loop, Quellmark Ridge Race, Ferncrest Dash, Ostrel Fitness, Verrin UK, Halden Leisure, Active Brookvale, Caswell Community Leisure, Lean Path Mentor, Vantor Labs and the Public Health Trust. The Norvate Pastimes team specialise in a bespoke, consultative approach for each project and pride ourselves in our attention to detail with passion and dedication.</p>
</section>

<section class="expertise">
  <h2 class="heading">We Are Expert In</h2>
  <div class="panel" style="left:0">
    <div class="panel-photo" role="img" aria-label="Heart rate line drawn in the shape of a heart" style="background:linear-gradient(135deg,#f4f4f4,#dcdcdc)"></div>
    <div class="panel-label">Health</div>
  </div>
  <div class="panel panel-feature" style="left:400px">
    <h3>Wellness</h3>
    <p>5 years experience working with some of the biggest global worldwide brands from equipment providers.</p>
    <div class="panel-more">More...</div>
  </div>
  <div class="panel" style="left:800px">
    <div class="panel-photo" role="img" aria-label="Athlete lifting a barbell in the gym" style="background:linear-gradient(135deg,#3a3a3a,#8a8a8a 55%,#d9d9d9)"></div>
    <div class="panel-label">Fitness</div>
  </div>
</section>

<section class="testimonial">
  <h2 class="heading">What Our Client Say</h2>
  <div class="quote-badge">
    <svg width="66" height="66" viewBox="0 0 66 66" aria-hidden="true"><g fill="#fff"><circle cx="26" cy="36" r="6"/><path d="M20 36 Q20 26 29 24 L29 27 Q24 29 24 34 Z"/><circle cx="41" cy="36" r="6"/><path d="M35 36 Q35 26 44 24 L44 27 Q39 29 39 34 Z"/></g></svg>
  </div>
  <p class="quote-text">" Quellmark Ridge Race and Norvate Pastimes first collaborated in 2015. Tavin and the Norvate team have showed impeccable drive, commitment, passion and integrity throughout our partnership. With the help of the Norvate team Ridge Race have gained huge success in the UK in 2015 and we are in great shape for 2016. Their ability to go to market quickly, professionally, with tenacity and high energy enables me to personally recommend the Norvate Pastimes organisation to anyone, or any company who requires a genuine, successful business collaboration and wants a great return on their investment "Highly Recommended"</p>
  <svg class="arrow" style="left:350px" width="16" height="34" viewBox="0 0 16 34" aria-hidden="true"><path d="M13 2 L3 17 L13 32" fill="none" stroke="#9a9a9a" stroke-width="2"/></svg>
  <div class="client">
    <div class="client-dot"></div>
    <div class="client-info">
      <div class="client-name">Tavin Marlowe -</div>
      <div class="client-role">Ridge Race CEO &amp; Founder of Ridge Race</div>
    </div>
  </div>
  <svg class="arrow" style="left:836px" width="16" height="34" viewBox="0 0 16 34" aria-hidden="true"><path d="M3 2 L13 17 L3 32" fill="none" stroke="#9a9a9a" stroke-width="2"/></svg>
</section>

<section class="services">
  <div class="services-bar"></div>
  <h2 class="heading">What We Do</h2>
  <div class="tile" style="left:0;background:linear-gradient(135deg,#6f6a5f,#b9ab95 60%,#e8e2d5)" role="img" aria-label="Seniors exercising with resistance bands"></div>
  <div class="tile tile-focus" style="left:300px;background:linear-gradient(160deg,#c47a74,#d9c8b4 50%,#8d9b86)" role="img" aria-label="Runners crossing an obstacle race course">
    <svg class="zoom" width="46" height="46" viewBox="0 0 46 46" aria-hidden="true"><circle cx="19" cy="19" r="14" fill="none" stroke="#fff" stroke-width="4"/><path d="M29 29 L42 42" stroke="#fff" stroke-width="5" stroke-linecap="round"/><path d="M12 19 H26 M19 12 V26" stroke="#fff" stroke-width="3"/></svg>
  </div>
  <div class="tile" style="left:600px;background:linear-gradient(135deg,#8a8a8a,#4d4d4d 55%,#2e2e2e)" role="img" aria-label="Athlete training with a barbell outdoors"></div>
  <div class="tile" style="left:900px;background:linear-gradient(135deg,#3c4b5d,#8c98a6 55%,#c9d0d6)" role="img" aria-label="Man doing a plank exercise on a mat"></div>
  <div class="services-rail">
    <svg class="abs" style="left:567px;top:18px" width="66" height="28" viewBox="0 0 66 28" aria-hidden="true"><path d="M16 4 L6 14 L16 24 M50 4 L60 14 L50 24" fill="none" stroke="#fff" stroke-width="3.5"/></svg>
  </div>
</section>

<section class="club">
  <div class="club-photo" role="img" aria-label="Smiling fitness couple holding a water bottle and exercise mat"></div>
  <h2 class="club-title">Join Our Health Club</h2>
  <p class="club-sub">A new type of obstacle course racing for the elite..</p>
  <div class="club-field" style="top:187px">Name*</div>
  <div class="club-field" style="top:254px">Email*</div>
  <div class="club-btn">Join Us Now</div>
</section>

<section class="consult" role="img" aria-label="Yellow toned photo of a gym floor behind the call to action">
  <h2 class="heading">We Provide You&nbsp; Facillity Of Consultancy</h2>
  <p class="consult-sub">Need a free quote, or have a question? Get in touch!</p>
  <div class="down">
    <svg width="62" height="62" viewBox="0 0 62 62" aria-hidden="true"><path d="M20 26 L31 37 L42 26" fill="none" stroke="#e9c60b" stroke-width="5" stroke-linecap="round" stroke-linejoin="round"/></svg>
  </div>
</section>

<footer class="footer">
  <h4 class="col-title" style="left:78px">Sitemap</h4>
  <ul class="sitemap">
    <li class="current">Home</li>
    <li>Health</li>
    <li>Wellness</li>
    <li>Fitness</li>
    <li>Our Team</li>
    <li>Testimonials</li>
    <li>Contact Us</li>
  </ul>

  <h4 class="col-title" style="left:340px">Latest News</h4>
  <div class="news" style="top:82px"><div class="news-thumb"></div><p>Lorem Ipsum is the simply dummy text of the print.</p><time>20 Oct 2017</time></div>
  <div class="news" style="top:172px"><div class="news-thumb"></div><p>Lorem Ipsum is the simply dummy text of the print.</p><time>20 Oct 2017</time></div>
  <div class="news" style="top:260px"><div class="news-thumb"></div><p>Lorem Ipsum is the simply dummy text of the print.</p><time>20 Oct 2017</time></div>

  <h4 class="col-title" style="left:608px">Contact Us</h4>
  <div class="contact-row" style="top:78px">
    <svg width="16" height="20" viewBox="0 0 16 20" aria-hidden="true"><path d="M8 1 C3.5 1 1 4.3 1 7.6 C1 12 8 19 8 19 C8 19 15 12 15 7.6 C15 4.3 12.5 1 8 1 Z" fill="none" stroke="#e9c60b" stroke-width="1.6"/><circle cx="8" cy="7.6" r="2.4" fill="#e9c60b"/></svg>
    <span>The Orchards, Wexmoor UK &amp;<br>Ireland</span>
  </div>
  <div class="contact-row" style="top:130px">
    <svg width="18" height="18" viewBox="0 0 18 18" aria-hidden="true"><path d="M4 1 L7 5 L5 7 Q7 11 11 13 L13 11 L17 14 L15 17 Q7 17 1 9 Q1 3 4 1 Z" fill="none" stroke="#e9c60b" stroke-width="1.5"/></svg>
    <span>07-500-419-226 &nbsp;&nbsp;or<br>01-600-738-145</span>
  </div>
  <div class="contact-row" style="top:188px">
    <svg width="18" height="14" viewBox="0 0 18 14" aria-hidden="true"><rect x="1" y="1" width="16" height="12" fill="none" stroke="#e9c60b" stroke-width="1.5"/><path d="M1 1 L9 8 L17 1" fill="none" stroke="#e9c60b" stroke-width="1.5"/></svg>
    <span>hello@norvatepastimes.com</span>
  </div>
  <div class="contact-row" style="top:228px">
    <svg width="18" height="18" viewBox="0 0 18 18" aria-hidden="true"><circle cx="9" cy="9" r="7.5" fill="none" stroke="#e9c60b" stroke-width="1.5"/><path d="M1.5 9 H16.5 M9 1.5 Q4 9 9 16.5 Q14 9 9 1.5" fill="none" stroke="#e9c60b" stroke-width="1.3"/></svg>
    <span>www.norvatepastimes.com</span>
  </div>
  <div class="contact-row" style="top:272px">
    <div class="social"></div>
    <div class="social"></div>
  </div>

  <div class="foot-brand">
    <div class="brand-name">Norvate Pastimes</div>
    <div class="brand-tag">Health, Wellness, Fitness, Consultants</div>
    <small><b>©Norvate Pastimes</b> - 2017 All Right<br>Reserved.</small>
  </div>
</footer>

</body>
</html>
```